Simon & Lorna's Yuletide Unwind Bash

Invitation to a party 60-80 people at a private residence. Age range 30-40s.

Themes: summer/casual/Australian backyard/local community

**For delivery via both email and printed copy**
Would like one document suitable for both purposes or two versions for electronic or paper invitation. I will arrange printing so please prepare it in a suitable format.

Specimen text attached. Address and phone contact to follow by message with successful bidder

Thanks!
Simon

Target Market(s)

Locals, friends. Party attendees will typicaly be parents in their forties who who be leaving the kids at home for a relaxed party night, and walking home afterward

Industry/Entity Type

Community

Font styles to use
Sans Serif

Requirements
Should not have
• Cliche Australiana imagery. No kangaroos etc

```html
<!DOCTYPE html>
<html lang="en">
<head>
<meta charset="utf-8">
<title>Simon & Lorna's Yuletide Unwind Bash – Invitation</title>
<link rel="stylesheet" href="https://fonts.googleapis.com/css2?family=Didact+Gothic&family=Lobster&family=Oswald:wght@500&family=Old+Standard+TT:wght@700&family=Roboto:wght@700&display=swap">
<style>
  :root {
    --page: #ffffff;
    --card-front: #f5f5f5;
    --festive-red: #dc0000;
    --ink: #333333;
    --ink-soft: #444444;
    --label-grey: #666666;
    --shadow: #cccccc;
    --white: #ffffff;
  }
  * { box-sizing: border-box; margin: 0; padding: 0; }
  html, body { width: 1200px; height: 1199px; overflow: hidden; background: var(--page); }
  .sheet { position: relative; width: 1200px; height: 1199px; border: 1px solid #e2e2e2; }

  .side-label {
    position: absolute; left: 207px;
    font-family: "Didact Gothic", sans-serif; font-size: 54px; color: var(--label-grey);
  }
  .side-label.front-label { top: 290px; }
  .side-label.back-label { top: 840px; }

  .card {
    position: absolute; left: 492px; width: 496px; height: 496px;
    box-shadow: 12px 12px 0 var(--shadow);
    overflow: hidden;
  }
  .card-front { top: 63px; background: var(--card-front); }
  .card-back { top: 626px; background: var(--festive-red); }

  .lights {
    position: absolute; left: 0; top: 52px; width: 496px; height: 136px;
    background: linear-gradient(180deg, rgba(220,0,0,0.08), rgba(220,0,0,0.22) 55%, rgba(220,0,0,0.06));
  }

  .ribbon { position: absolute; left: 49px; top: 41px; width: 397px; height: 30px; }
  .ribbon svg { position: absolute; inset: 0; }
  .ribbon-text {
    position: absolute; inset: 0; display: flex; align-items: center; justify-content: space-between;
    padding: 0 16px 0 20px;
    font-family: "Oswald", sans-serif; font-size: 16px; color: var(--white); letter-spacing: -0.3px;
    text-transform: uppercase;
  }
  .ribbon-amp { font-family: "Lobster", cursive; font-size: 28px; width: 40px; text-align: center; }

  .title {
    position: absolute; left: 0; width: 100%; text-align: center;
    font-family: "Lobster", cursive; color: var(--festive-red); line-height: 1;
  }
  .title-names { top: 188px; font-size: 54px; }
  .title-event { top: 253px; font-size: 52px; }

  .line-text {
    position: absolute; left: 0; width: 100%; text-align: center;
    font-family: "Didact Gothic", sans-serif; color: var(--ink-soft);
  }
  .audience { top: 318px; font-size: 20px; letter-spacing: 1.2px; }
  .address { top: 452px; font-size: 20px; letter-spacing: 1.6px; }

  .ruled {
    position: absolute; left: 28px; width: 440px; display: flex; align-items: center; gap: 10px;
    font-family: "Roboto", sans-serif; font-weight: 700; font-size: 21px; color: var(--festive-red);
    white-space: nowrap;
  }
  .ruled::before, .ruled::after { content: ""; flex: 1; height: 3px; background: var(--festive-red); }
  .ruled-day { top: 344px; }
  .ruled-time { top: 424px; }

  .date {
    position: absolute; left: 0; width: 100%; top: 365px; text-align: center;
    font-family: "Old Standard TT", serif; font-weight: 700; font-size: 58px; color: var(--ink); letter-spacing: 1px;
  }

  .dotted-rule {
    position: absolute; left: 50px; width: 400px; height: 4px;
    background-image: radial-gradient(circle, var(--white) 1.8px, transparent 2px);
    background-size: 16px 4px; background-repeat: repeat-x;
  }
  .dotted-rule.top { top: 150px; }
  .dotted-rule.bottom { top: 344px; }

  .details {
    position: absolute; left: 30px; width: 436px; top: 176px; list-style: none; text-align: center;
    font-family: "Didact Gothic", sans-serif; font-size: 12.6px; line-height: 14px; color: var(--white);
  }
  .details li { margin-bottom: 6.5px; }
  .details li::before {
    content: ""; display: inline-block; width: 8px; height: 8px; border-radius: 50%;
    background: var(--white); margin-right: 5px; vertical-align: 0px;
  }
</style>
</head>
<body>
<div class="sheet">
  <div class="side-label front-label">Front</div>
  <div class="side-label back-label">Back</div>

  <section class="card card-front">
    <div class="lights" role="img" aria-label="Strands of red festive string lights draped across the top of the card"></div>

    <div class="ribbon">
      <svg width="397" height="30" viewBox="0 0 397 30" aria-hidden="true">
        <polygon points="0,0 397,0 387,15 397,30 0,30 10,15" fill="var(--festive-red)"/>
        <circle cx="199" cy="16" r="29" fill="var(--festive-red)"/>
      </svg>
      <div class="ribbon-text">
        <span>Leave the kids at home</span>
        <span class="ribbon-amp">&amp;</span>
        <span>Let your hair down at</span>
      </div>
    </div>

    <h1 class="title title-names">Simon &amp; Lorna's</h1>
    <h2 class="title title-event">Yuletide Unwind Bash</h2>

    <p class="line-text audience">For Kinsella Heights and friends</p>
    <div class="ruled ruled-day">Saturday</div>
    <div class="date">02.01.2016</div>
    <div class="ruled ruled-time">From 6pm 'til late</div>
    <p class="line-text address">25 Wattlebrook Street, Kinsella Heights</p>
  </section>

  <section class="card card-back">
    <div class="dotted-rule top"></div>
    <ul class="details">
      <li>Child-free event</li>
      <li>Dress: summer casual, bare feet welcome</li>
      <li>Cocktail food provided</li>
      <li>BYO but only if you insist</li>
      <li>If you have some friends or neighbours that you like<br>to hang out with, we would love to meet. Bring them with you!</li>
      <li>An RSVP for catering would be nice.<br>Text Simon xxx xxxxxx or Lorna yyyyyyyy before Xmas please.</li>
    </ul>
    <div class="dotted-rule bottom"></div>
  </section>
</div>
</body>
</html>
```